Business Card for premium dental clinic

We are a premium dental clinic based in Brasov, Romania with more than 15 year on the market, providing quality dental treatment made by a team of more specialized dentists, working with modern equipment as a solution to beautiful and healthy teeth.

Our current logo for the clinic use 2 square with colors black and gold - dr Corbescu - studio, using family fonts Bodoni, Myriad Pro and Segoe Print.
Depending on the printing we used some gold CMYK background or gold foil picture background or a gold gradient.
We want a business card:
- eye catching business card
- distinguished business card
- premium design
- to keep the color scheme of black and gold
- to attract the customers to spent time reading the information
- modern concept

```html
<!DOCTYPE html>
<html lang="en">
<head>
<meta charset="utf-8">
<title>dr Corbescu – business card</title>
<link rel="stylesheet" href="https://fonts.googleapis.com/css2?family=Lato:wght@400;700;900&family=Oswald:wght@600&display=swap">
<style>
  :root {
    --gold: #bb8b2a;
    --black: #0b0b0b;
    --ink: #1d1d1d;
    --paper-front: #fbf6f6;
    --paper-back: #ffffff;
    --rule: #9a9a9a;
    --stage: #e6e6e6;
  }
  * { box-sizing: border-box; margin: 0; padding: 0; }
  html, body { width: 1200px; height: 782px; overflow: hidden; }
  body {
    background: var(--stage);
    font-family: "Lato", Arial, sans-serif;
    color: var(--ink);
    display: flex;
    align-items: center;
    justify-content: center;
    gap: 40px;
  }
  .card {
    position: relative;
    width: 540px;
    height: 309px;
    overflow: hidden;
    box-shadow: 0 6px 18px rgba(0,0,0,.18);
  }
  .card--front { background: var(--paper-front); }
  .card--back { background: var(--paper-back); }
  .card__bands { position: absolute; left: 0; bottom: 0; width: 540px; height: 24px; }

  /* Front */
  .brand-name {
    position: absolute; left: 40px; top: 128px;
    width: 236px;
    font-family: "Lato", Arial, sans-serif;
    font-weight: 700; font-size: 28px; line-height: 1;
    color: var(--black);
    white-space: nowrap;
  }
  .divider {
    position: absolute; left: 292px; top: 86px;
    width: 1px; height: 118px; background: var(--rule);
  }
  .contact { position: absolute; left: 312px; top: 84px; }
  .contact__name {
    font-weight: 900; font-size: 19px; letter-spacing: .5px;
    color: var(--gold); text-transform: uppercase; line-height: 1;
  }
  .contact__role { font-size: 14px; margin: 3px 0 8px; }
  .contact__list { list-style: none; font-size: 14.5px; line-height: 1.38; }
  .contact__list li { display: flex; align-items: center; gap: 6px; }
  .contact__list svg { width: 12px; height: 12px; flex: none; fill: var(--gold); }

  /* Back */
  .appointment { position: absolute; left: 44px; right: 44px; top: 40px; }
  .appointment__title {
    font-family: "Oswald", "Arial Narrow", sans-serif;
    font-weight: 600; font-size: 27px; text-align: center;
    letter-spacing: .3px; color: var(--black); margin-bottom: 14px;
  }
  .field {
    display: block; font-size: 14px; letter-spacing: .5px;
    padding: 10px 0 2px; border-bottom: 1px solid var(--rule);
  }
  .appointment__note { font-size: 13px; text-align: center; margin-top: 22px; }
</style>
</head>
<body>

  <section class="card card--front" aria-label="Business card front">
    <p class="brand-name">dr Corbescu</p>
    <span class="divider"></span>
    <div class="contact">
      <p class="contact__name">Andrei Marinescu</p>
      <p class="contact__role">Managing Director</p>
      <ul class="contact__list">
        <li><svg viewBox="0 0 12 12"><path d="M1 3c0-1 1-2 2-2h6c1 0 2 1 2 2v1H8V3H4v1H1zM2 5h8l1 6H1z"/></svg>040-268 410 732</li>
        <li><svg viewBox="0 0 12 12"><path d="M0 2h12v1L6 7 0 3zM0 4.3l6 4 6-4V10H0z"/></svg>info@corbescudental.com</li>
        <li><svg viewBox="0 0 12 12"><circle cx="6" cy="6" r="6"/></svg>www.corbescudental.com</li>
        <li>421, Address line here</li>
        <li>Country Name, 45452</li>
      </ul>
    </div>
    <svg class="card__bands" viewBox="0 0 540 24" aria-hidden="true">
      <polygon points="0,10 276,10 270,24 0,24" fill="var(--gold)"/>
      <polygon points="284,2 540,2 540,24 270,24" fill="var(--black)"/>
    </svg>
  </section>

  <section class="card card--back" aria-label="Business card back">
    <div class="appointment">
      <h1 class="appointment__title">YOUR NEXT APPOINTMENT</h1>
      <span class="field">NAME</span>
      <span class="field">TIME</span>
      <p class="appointment__note">If unable to keep appointment, kindly give 24hrs notice.</p>
    </div>
    <svg class="card__bands" viewBox="0 0 540 24" aria-hidden="true">
      <polygon points="0,10 276,10 270,24 0,24" fill="var(--gold)"/>
      <polygon points="284,2 540,2 540,24 270,24" fill="var(--black)"/>
    </svg>
  </section>

</body>
</html>
```